TIMBER DECK COMPANY FLYER

We need a flyer design for a Timber Decking company, we specialise in timber decks, stairs, privacy screens, maintenance and pergolas. I have attatched some pictures which you can incorporate if you think they need cropping go for it. We offer amazing decks at affordable prices by qualified tradespeople.
My logo is a dull green I would like this to be changed to a more lime bright green please. Also my logo is too big I would like this logo halved in size please. And the colours in the brochure maybe a blackbackground with lime green and other colours you think will work. We will also beat any reputable Decking companies quote by 10%. Our decks add style, class, longjevity and practicality to any home. The final design should be modern and cutting edge.

Target Market(s)

home owners

Industry/Entity Type

It Company

Logo Text

CEDARLINE PATIO WORKS

Requirements
Must have
• DECKS
STAIRS
PERGOLAS
PRIVACY SCREENS
DECK MAINTENANCE

CONTACT-GORDON-0427158302

MUST HAVE LIKE US ON LINKSPACE LOGO

www.cedarlinepatioworks.com.au
Nice to have
• Please let me know if need more photos etc

```html
<!DOCTYPE html>
<html lang="en">
<head>
<meta charset="utf-8">
<title>Cedarline Patio Works – Flyer</title>
<link rel="stylesheet" href="https://fonts.googleapis.com/css2?family=Anton&family=Oswald:wght@500;700&display=swap">
<style>
  :root {
    --lime: #c8e81e;
    --lime-deep: #b4d312;
    --ink: #0d0d0d;
    --paper: #ffffff;
    --label-text: #d4f02a;
    --wood-light: #c99a72;
    --wood-mid: #a86f4c;
    --wood-dark: #7d4c32;
  }
  * { box-sizing: border-box; margin: 0; padding: 0; }
  html, body { width: 1200px; height: 930px; overflow: hidden; background: var(--paper); }
  .flyer { position: relative; width: 1200px; height: 930px; overflow: hidden; background: var(--paper); }

  /* Header */
  .masthead { position: absolute; left: 0; top: 0; width: 1200px; height: 195px; background: var(--paper); }
  .brand-mark { position: absolute; left: 48px; top: 40px; width: 130px; height: 130px; background: var(--lime); }
  .brand-name {
    position: absolute; left: 240px; top: 22px; width: 910px;
    font-family: "Anton", sans-serif; font-weight: 400; color: var(--ink);
    text-align: right; line-height: 1;
  }
  .brand-name .line-one { display: block; font-size: 100px; letter-spacing: 1px; }
  .brand-name .line-two { display: block; font-size: 52px; letter-spacing: 42px; margin-top: 8px; margin-right: -42px; }

  /* Lime band */
  .services-band {
    position: absolute; left: 0; top: 195px; width: 1200px; height: 570px;
    background: linear-gradient(180deg, var(--lime-deep) 0%, var(--lime) 6%, var(--lime) 100%);
  }
  .photo {
    position: absolute; width: 331px; height: 245px;
    box-shadow: 0 0 0 8px var(--lime), 4px 6px 12px rgba(0,0,0,.35);
  }
  .photo--stairs   { left: 52px;  top: 30px;  background: linear-gradient(160deg, #3f6b34, #b79a72 55%, #d8c6a4); }
  .photo--deck     { left: 52px;  top: 287px; background: linear-gradient(180deg, #6f7a6a 0%, #8e3f26 35%, #a3492c 100%); }
  .photo--plunge   { left: 810px; top: 30px;  background: linear-gradient(180deg, #5d5f5c 0%, #1f2c2e 40%, #2b3a3a 75%, #b5532e 100%); }
  .photo--poolside { left: 810px; top: 287px; background: linear-gradient(100deg, #4f7a3a 0%, #a4552f 35%, #d8d2c4 55%, #3aa3d9 80%); }

  .tag {
    position: absolute; top: 235px; height: 87px; background: var(--ink);
    color: var(--label-text); font-family: "Oswald", sans-serif; font-weight: 700;
    font-size: 15px; line-height: 21px; text-align: center; text-transform: uppercase;
    display: flex; align-items: center; justify-content: center;
  }
  .tag--price { left: 0; width: 266px; }
  .tag--promise { left: 925px; width: 275px; }

  .service-list {
    position: absolute; left: 398px; top: 30px; width: 400px; list-style: none;
    font-family: "Anton", sans-serif; font-size: 44px; color: var(--ink);
    text-align: center; line-height: 1.1;
  }
  .service-list li { margin-bottom: 45px; }
  .service-list li.two-line { line-height: 1.4; }

  /* Footer */
  .footer { position: absolute; left: 0; top: 765px; width: 1200px; height: 165px; }
  .footer-surface {
    position: absolute; inset: 0;
    background: linear-gradient(90deg, var(--wood-light), var(--wood-mid) 45%, var(--wood-light) 70%, var(--wood-dark));
  }
  .footer-wash { position: absolute; left: 0; top: 30px; width: 1200px; height: 105px; background: rgba(255,255,255,.45); }
  .contact {
    position: absolute; left: 150px; top: 46px; width: 510px;
    font-family: "Oswald", sans-serif; font-weight: 700; color: var(--ink);
    font-size: 28px; line-height: 42px; text-align: center;
  }
  .social-badge {
    position: absolute; left: 835px; top: 38px; width: 288px; height: 88px;
    background: var(--paper); border-radius: 10px;
    display: flex; align-items: center; gap: 16px; padding: 0 16px;
  }
  .social-badge .dot { width: 58px; height: 58px; background: #2a5aa8; border-radius: 8px; flex: none; }
  .social-badge .cta { font-family: "Oswald", sans-serif; font-weight: 500; font-size: 26px; color: #2a5aa8; line-height: 1.1; }
</style>
</head>
<body>
<div class="flyer">
  <header class="masthead">
    <div class="brand-mark"></div>
    <h1 class="brand-name"><span class="line-one">CEDARLINE PATIO</span><span class="line-two">WORKS</span></h1>
  </header>

  <section class="services-band">
    <div class="photo photo--stairs" role="img" aria-label="Timber staircase with balustrade beside garden foliage"></div>
    <div class="photo photo--deck" role="img" aria-label="Red hardwood deck curving around a pool"></div>
    <div class="photo photo--plunge" role="img" aria-label="Plunge pool surrounded by hardwood decking and sandstone planters"></div>
    <div class="photo photo--poolside" role="img" aria-label="Narrow timber deck path beside a blue pool and glass fence"></div>

    <p class="tag tag--price">We will beat any<br>reputable decking<br>companies quote by 10%.</p>
    <p class="tag tag--promise">Our decks add style, class,<br>longevity and practicality<br>to any home.</p>

    <ul class="service-list">
      <li>DECKS</li>
      <li>STAIRS</li>
      <li>PERGOLAS</li>
      <li>PRIVACY SCREENS</li>
      <li class="two-line">DECK<br>MAINTENANCE</li>
    </ul>
  </section>

  <footer class="footer">
    <div class="footer-surface" role="img" aria-label="Close-up of hardwood deck boards"></div>
    <div class="footer-wash"></div>
    <p class="contact">CONTACT GORDON 0427158302<br>www.cedarlinepatioworks.com.au</p>
    <div class="social-badge">
      <span class="dot"></span>
      <span class="cta">“like” us on<br>Linkspace</span>
    </div>
  </footer>
</div>
</body>
</html>
```